Laundry Store front design

I own a laundry business and require a design for the shop front.

I have uploaded 3 photos with window numbers on, 1 thru 5. It might be better to stich these together as I want the design to flow across 1-5 but only the top of 3.

I have uploaded some pdf documents with more details.

Font styles to use
Serif

Colors
0054AA
0677BA
7BADD7
CADEEF
E8F1F8

```html
<!DOCTYPE html>
<html lang="en">
<head>
<meta charset="utf-8">
<title>Harbor Laundry Services – Shop Front Windows</title>
<link href="https://fonts.googleapis.com/css2?family=Poppins:wght@400;500;600;700;800&display=swap" rel="stylesheet">
<style>
  :root{
    --blue-deep:#0054AA;
    --blue:#0677BA;
    --blue-bright:#2C8FD8;
    --blue-soft:#7BADD7;
    --blue-pale:#CADEEF;
    --blue-mist:#E8F1F8;
    --ink:#15202E;
    --white:#FFFFFF;
    --green:#3A9E3F;
    --page:#EEF2F6;
  }
  *{box-sizing:border-box;margin:0;padding:0}
  html,body{width:1200px;height:2621px;overflow:hidden}
  body{background:var(--page);font-family:'Poppins',Arial,sans-serif;color:var(--ink);position:relative}

  .window{position:absolute;background:var(--page)}
  .band{position:absolute;left:0;top:0;width:100%;display:block}
  .pane{position:absolute;overflow:hidden;background:var(--white)}
  .mullion{position:absolute;background:var(--page)}
  .photo{position:absolute}

  .brand{display:block;text-align:center;color:var(--blue);line-height:1}
  .brand-name{display:block;font-weight:500;font-size:27px;letter-spacing:.5px;color:var(--blue)}
  .brand-sub{display:block;font-weight:400;font-size:8px;letter-spacing:1px;margin-top:2px;color:var(--blue)}
  .brand.on-blue .brand-name,.brand.on-blue .brand-sub{color:var(--white)}

  .ticks{list-style:none}
  .ticks li{position:relative;padding-left:13px;line-height:1.15}
  .ticks li::before{content:"";position:absolute;left:0;top:.25em;width:9px;height:9px;border-radius:50%;background:var(--blue)}
  .ticks li::after{content:"";position:absolute;left:3px;top:calc(.25em + 2px);width:2px;height:4px;border:solid var(--white);border-width:0 1.5px 1.5px 0;transform:rotate(45deg)}
  .ticks.light li::before{background:var(--white)}
  .ticks.light li::after{border-color:var(--blue)}

  .headline{font-weight:800;line-height:1}
  .center{text-align:center}
  .circle{position:absolute;border-radius:50%}
</style>
</head>
<body>

<!-- WINDOW 1 -->
<section class="window" style="left:62px;top:265px;width:512px;height:410px">
  <svg class="band" width="512" height="105" viewBox="0 0 512 105" preserveAspectRatio="none">
    <defs>
      <linearGradient id="w1g" x1="0" x2="1"><stop offset="0" stop-color="#2C8FD8"/><stop offset="1" stop-color="#0677BA"/></linearGradient>
    </defs>
    <rect width="512" height="105" fill="url(#w1g)"/>
    <path d="M0 105 L0 92 C120 96 200 40 300 42 C380 44 430 70 512 62 L512 105Z" fill="#fff"/>
    <path d="M190 22 C260 18 330 40 380 60 C420 76 470 72 512 58" stroke="#15202E" stroke-width="6" fill="none"/>
    <circle cx="344" cy="26" r="9" fill="#0677BA" stroke="#fff" stroke-width="3"/>
  </svg>
  <div class="mullion" style="left:184px;top:0;width:6px;height:105px"></div>
  <div class="mullion" style="left:372px;top:0;width:6px;height:105px"></div>
  <div class="mullion" style="left:0;top:105px;width:512px;height:8px"></div>
  <div class="mullion" style="left:180px;top:113px;width:6px;height:297px"></div>
  <div class="mullion" style="left:356px;top:113px;width:22px;height:297px"></div>

  <div class="pane" style="left:0;top:113px;width:180px;height:297px">
    <div class="brand" style="margin-top:24px"><span class="brand-name">harbor</span><span class="brand-sub">Laundry Services</span></div>
    <p class="center" style="margin-top:18px;font-size:12px;font-weight:500;letter-spacing:-.2px">CLEANING EXCELLENCE</p>
    <p class="center headline" style="font-size:19px;color:var(--blue)">GUARANTEED</p>
    <div class="circle" style="left:16px;top:135px;width:50px;height:50px;background:var(--blue-bright)"></div>
    <div class="photo" role="img" aria-label="Smiling laundry worker in apron holding an armful of clothes" style="left:30px;top:140px;width:150px;height:157px;background:linear-gradient(180deg,#d9c3ae,#7fc0c6)"></div>
  </div>

  <div class="pane" style="left:186px;top:113px;width:170px;height:297px">
    <div class="circle" style="left:10px;top:26px;width:150px;height:150px;background:var(--blue)"></div>
    <div style="position:absolute;left:22px;top:50px;width:126px;color:var(--white)">
      <p class="center headline" style="font-size:12.5px;font-weight:700">SPECIAL<br>PRICING FOR</p>
      <ul class="ticks light" style="margin-top:5px;font-size:9.5px;padding-left:4px">
        <li>Property managers</li><li>Hotels</li><li>Apartments</li><li>Villas</li><li>Restaurants</li>
      </ul>
      <p style="font-size:9.5px;padding-left:17px">and more</p>
    </div>
    <div class="circle" style="left:-20px;top:190px;width:120px;height:110px;background:#8fc9cc;opacity:.7"></div>
    <div class="circle" style="left:60px;top:200px;width:76px;height:76px;background:linear-gradient(135deg,#7BADD7,#2C8FD8)"></div>
  </div>

  <div class="pane" style="left:378px;top:113px;width:134px;height:297px">
    <div style="position:absolute;left:0;top:0;width:134px;height:140px;background:var(--blue);color:var(--white);padding-top:18px" class="center">
      <p class="headline" style="font-size:19px;font-weight:800">SPECIAL<br>PRICING</p>
      <p style="font-size:16px;font-weight:500;margin-top:6px">Starting at</p>
      <p class="headline" style="font-size:32px"><sup style="font-size:16px">$</sup>150</p>
    </div>
    <div class="photo" role="img" aria-label="Cheerful woman in apron presenting with one hand while holding laundry" style="left:0;top:140px;width:134px;height:157px;background:linear-gradient(180deg,#ffffff 0%,#ffffff 20%,#a7bfd3 100%)"></div>
  </div>
</section>

<!-- WINDOW 2 -->
<section class="window" style="left:630px;top:285px;width:475px;height:380px">
  <svg class="band" width="475" height="100" viewBox="0 0 475 100" preserveAspectRatio="none">
    <rect width="475" height="100" fill="#fff"/>
    <path d="M0 55 C60 50 100 75 150 85 L150 100 L0 100Z" fill="#2C8FD8"/>
    <path d="M135 100 L135 70 C190 95 250 95 300 70 L300 100Z" fill="#2C8FD8"/>
    <path d="M300 60 C350 45 390 35 475 25 L475 0 L300 0Z" fill="#0677BA"/>
    <path d="M300 0 L475 0 L475 18 C400 20 360 30 330 45 C315 52 305 50 300 48Z" fill="#2C8FD8"/>
    <path d="M305 40 C340 50 380 30 475 22" stroke="#15202E" stroke-width="5" fill="none"/>
    <circle cx="338" cy="40" r="7" fill="#0677BA" stroke="#fff" stroke-width="2"/>
    <circle cx="372" cy="44" r="16" fill="#7BADD7" stroke="#0677BA" stroke-width="3"/>
  </svg>
  <div class="mullion" style="left:125px;top:0;width:10px;height:100px"></div>
  <div class="mullion" style="left:295px;top:0;width:10px;height:100px"></div>
  <div class="mullion" style="left:0;top:100px;width:475px;height:6px"></div>
  <div class="brand" style="position:absolute;left:135px;top:24px;width:160px"><span class="brand-name">harbor</span><span class="brand-sub">Laundry Services</span></div>

  <div class="pane" style="left:0;top:106px;width:125px;height:138px;background:var(--blue)">
    <p class="headline" style="position:absolute;left:10px;top:12px;color:var(--white);font-size:27px">FREE</p>
    <p class="headline" style="position:absolute;left:10px;top:40px;color:var(--white);font-size:15px;font-weight:700">DELIVERY</p>
    <p style="position:absolute;left:10px;top:58px;color:var(--white);font-size:6px;line-height:1.1">within<br>local<br>area</p>
    <div style="position:absolute;left:0;top:70px;width:125px;height:68px;background:var(--white);border-radius:50% 50% 0 0/30% 30% 0 0"></div>
    <div class="photo" role="img" aria-label="Illustration of a delivery rider on a yellow scooter" style="left:35px;top:60px;width:70px;height:66px;background:radial-gradient(circle at 50% 60%,#f2b632 0 40%,#e8f1f8 70%)"></div>
  </div>
  <div class="mullion" style="left:0;top:244px;width:125px;height:6px"></div>
  <div class="pane" style="left:0;top:250px;width:125px;height:130px">
    <div class="photo" role="img" aria-label="White front-loading washing machine" style="left:35px;top:8px;width:55px;height:65px;background:linear-gradient(180deg,#f4f6f8,#c9d3dc)"></div>
    <div style="position:absolute;left:0;top:70px;width:125px;height:60px;background:var(--blue);border-radius:50% 50% 0 0/40% 40% 0 0"></div>
    <p class="center headline" style="position:absolute;left:0;top:84px;width:125px;color:var(--white);font-size:17px;font-weight:700">BOOK<br>ONLINE</p>
  </div>
  <div class="mullion" style="left:125px;top:106px;width:15px;height:274px"></div>

  <div class="pane" style="left:140px;top:106px;width:165px;height:274px">
    <p class="headline" style="position:absolute;left:18px;top:18px;font-size:56px;color:var(--blue)">20</p>
    <p class="headline" style="position:absolute;left:92px;top:20px;font-size:24px;color:var(--blue)">%</p>
    <p class="headline" style="position:absolute;left:96px;top:48px;font-size:15px;font-weight:700">OFF</p>
    <p class="headline" style="position:absolute;left:16px;top:76px;font-size:22px;font-weight:800">DISCOUNT</p>
    <p class="center" style="position:absolute;left:16px;top:102px;width:130px;background:var(--blue);color:var(--white);font-size:9.5px;font-weight:600;letter-spacing:2.5px;padding:1px 0">FIRST ORDER</p>
    <p class="center" style="position:absolute;left:0;top:124px;width:165px;font-size:7px;font-weight:600">www.harborlaundry.example</p>
    <div class="photo" role="img" aria-label="Child peeking out of a colourful pile of clothes" style="left:0;top:150px;width:165px;height:124px;background:linear-gradient(180deg,#fff 0%,#f5c7a0 30%,#e88a6a 60%,#5fb7d8 100%)"></div>
  </div>
  <div class="pane" style="left:310px;top:106px;width:160px;height:274px">
    <div class="photo" role="img" aria-label="Smiling woman holding a wicker basket of folded laundry" style="left:0;top:0;width:160px;height:274px;background:linear-gradient(180deg,#e6e0d6 0%,#d9d1c4 40%,#c46a3c 70%,#b89466 100%)"></div>
  </div>
</section>

<!-- WINDOW 3 -->
<section class="window" style="left:300px;top:1095px;width:605px;height:480px">
  <svg class="band" width="605" height="130" viewBox="0 0 605 130" preserveAspectRatio="none">
    <rect width="605" height="130" fill="#fff"/>
    <path d="M0 130 L0 45 C60 30 120 70 175 80 L175 130Z" fill="#2C8FD8"/>
    <path d="M175 130 L175 95 C260 110 320 110 400 95 L400 130Z" fill="#2C8FD8"/>
    <path d="M400 130 L400 85 C460 70 540 55 605 40 L605 130Z" fill="#2C8FD8"/>
    <circle cx="445" cy="60" r="24" fill="#fff"/>
    <circle cx="445" cy="60" r="19" fill="#7BADD7" stroke="#0677BA" stroke-width="2"/>
  </svg>
  <div class="mullion" style="left:0;top:0;width:10px;height:480px"></div>
  <div class="mullion" style="left:175px;top:0;width:10px;height:130px"></div>
  <div class="mullion" style="left:390px;top:0;width:10px;height:130px"></div>
  <div class="mullion" style="left:595px;top:0;width:10px;height:480px"></div>
  <div class="mullion" style="left:0;top:130px;width:605px;height:7px"></div>
  <div class="brand" style="position:absolute;left:185px;top:30px;width:205px"><span class="brand-name" style="font-size:30px">harbor</span><span class="brand-sub">Laundry Services</span></div>

  <div class="pane" style="left:10px;top:137px;width:145px;height:168px;background:var(--blue-bright)">
    <div class="brand on-blue" style="margin-top:62px"><span class="brand-name">harbor</span><span class="brand-sub">Laundry Services</span></div>
  </div>
  <div class="mullion" style="left:10px;top:305px;width:145px;height:10px"></div>
  <div class="pane" style="left:10px;top:315px;width:145px;height:160px">
    <p style="margin:14px 0 0 12px;font-size:19px;font-weight:500;line-height:1">HOURS OF</p>
    <p class="headline" style="margin-left:12px;font-size:22px;color:var(--blue)">OPENING</p>
    <table style="margin:10px 0 0 12px;width:122px;border-collapse:collapse;font-size:7.5px;font-weight:600">
      <tr style="background:var(--blue);color:var(--white)"><td style="padding:1px 4px">MON - FRI</td><td>9.00-6.00</td></tr>
      <tr><td style="padding:1px 4px">SAT</td><td>9.00-5.00</td></tr>
      <tr style="background:var(--blue);color:var(--white)"><td style="padding:1px 4px">SUN</td><td>CLOSED</td></tr>
    </table>
    <p style="margin:8px 0 0 12px;font-size:14px;font-weight:700;display:flex;align-items:center;gap:3px">
      <svg width="12" height="12" viewBox="0 0 24 24"><path d="M6.6 10.8a15.5 15.5 0 0 0 6.6 6.6l2.2-2.2a1 1 0 0 1 1-.25 11.4 11.4 0 0 0 3.6.57 1 1 0 0 1 1 1V20a1 1 0 0 1-1 1A17 17 0 0 1 3 4a1 1 0 0 1 1-1h3.5a1 1 0 0 1 1 1c0 1.25.2 2.45.57 3.57a1 1 0 0 1-.25 1Z" fill="#15202E"/></svg>555 012 3456</p>
  </div>
  <div class="mullion" style="left:155px;top:137px;width:35px;height:343px"></div>

  <div class="pane" style="left:190px;top:137px;width:200px;height:338px">
    <ul class="ticks" style="position:absolute;left:14px;top:14px;font-size:9.5px;width:80px">
      <li>Service<br>washes</li><li>Ironing<br>service</li><li>duvets</li><li>linen</li><li>towels</li>
    </ul>
    <ul class="ticks" style="position:absolute;left:95px;top:14px;font-size:9.5px;width:100px">
      <li>wedding<br>dresses</li><li>upholstery</li><li>rugs</li><li>collection<br>&amp; delivery</li>
    </ul>
    <div style="position:absolute;left:0;top:170px;width:200px;height:168px;background:var(--blue-bright);border-radius:0 70% 0 0/0 40% 0 0"></div>
    <div class="photo" role="img" aria-label="Young woman carrying an armful of clothes" style="left:20px;top:120px;width:160px;height:218px;background:linear-gradient(180deg,#f1e3d7 0%,#3a3a44 45%,#f0d68a 70%,#2f3340 100%);opacity:.9"></div>
    <div class="circle" style="left:25px;top:170px;width:44px;height:44px;background:var(--blue-soft);border:3px solid var(--white)"></div>
  </div>
  <div class="pane" style="left:400px;top:137px;width:195px;height:338px">
    <div class="photo" role="img" aria-label="Woman smelling fresh laundry in a basket against a pink backdrop" style="left:0;top:0;width:195px;height:338px;background:linear-gradient(180deg,#f6c9cf 0%,#f3bfc6 45%,#c9d6ea 75%,#f1f3f6 100%)"></div>
  </div>
</section>

<!-- WINDOW 4 -->
<section class="window" style="left:80px;top:1905px;width:550px;height:425px">
  <svg class="band" width="550" height="105" viewBox="0 0 550 105" preserveAspectRatio="none">
    <rect width="550" height="105" fill="#fff"/>
    <path d="M0 0 L160 0 L160 20 C100 15 40 22 0 30Z" fill="#2C8FD8"/>
    <path d="M0 105 L0 95 C60 90 120 98 160 100 L160 105Z" fill="#2C8FD8"/>
    <path d="M170 0 L350 0 L350 105 L330 105 C300 70 250 50 170 45Z" fill="#2C8FD8"/>
    <path d="M370 0 L545 0 L545 60 C520 40 480 30 440 45 C400 60 390 20 370 10Z" fill="#2C8FD8"/>
    <path d="M370 105 L370 80 C400 90 420 100 440 105Z" fill="#2C8FD8"/>
  </svg>
  <div class="mullion" style="left:0;top:0;width:5px;height:425px"></div>
  <div class="mullion" style="left:160px;top:0;width:10px;height:105px"></div>
  <div class="mullion" style="left:258px;top:10px;width:6px;height:95px"></div>
  <div class="mullion" style="left:350px;top:0;width:20px;height:105px"></div>
  <div class="mullion" style="left:545px;top:0;width:5px;height:425px"></div>
  <div class="mullion" style="left:0;top:105px;width:550px;height:10px"></div>
  <p class="center" style="position:absolute;left:5px;top:48px;width:155px;font-size:17px;font-weight:700;color:var(--green);line-height:1">PureRinse</p>
  <p class="center" style="position:absolute;left:5px;top:68px;width:155px;font-size:6px;letter-spacing:1.5px;color:var(--blue)">WET CLEANING</p>
  <p class="center" style="position:absolute;left:385px;top:52px;width:155px;font-size:17px;font-weight:700;color:var(--green);line-height:1">PureRinse</p>
  <p class="center" style="position:absolute;left:385px;top:72px;width:155px;font-size:6px;letter-spacing:1.5px;color:var(--blue)">WET CLEANING</p>

  <div class="pane" style="left:5px;top:115px;width:145px;height:310px;background:var(--blue-bright)">
    <div style="position:absolute;left:0;top:0;width:145px;height:150px;background:var(--white);border-radius:0 0 60% 0/0 0 40% 0"></div>
    <div class="photo" role="img" aria-label="Smiling man holding a pile of laundry" style="left:0;top:20px;width:130px;height:290px;background:linear-gradient(180deg,#e8c9b2 0%,#dfe6ee 40%,#9cb7d8 65%,#d9c1a0 100%)"></div>
    <div class="circle" style="left:78px;top:62px;width:44px;height:44px;background:var(--blue-soft);border:3px solid var(--white)"></div>
  </div>
  <div class="mullion" style="left:5px;top:255px;width:145px;height:8px"></div>
  <div class="mullion" style="left:150px;top:115px;width:20px;height:310px"></div>

  <div class="pane" style="left:170px;top:115px;width:190px;height:310px">
    <p class="center" style="margin-top:24px;font-size:23px;font-weight:700;color:var(--green);line-height:1">PureRinse</p>
    <p class="center" style="margin-top:3px;font-size:11px;letter-spacing:2.5px;color:var(--blue)">WET CLEANING</p>
    <div style="margin:4px auto 0;width:140px;height:1.5px;background:var(--blue)"></div>
    <div style="margin:3px auto 0;width:30px;height:8px;border-radius:4px;background:var(--blue)"></div>
    <ul class="ticks" style="margin:12px 0 0 26px;font-size:9.5px;width:150px">
      <li style="margin-bottom:7px">Specially adapted<br>machines</li>
      <li style="margin-bottom:7px">Eco-friendly, no harsh<br>chemicals</li>
      <li style="margin-bottom:7px">VIP 2 hour service<br>available</li>
      <li style="margin-bottom:7px">Superior stain removal</li>
      <li>Suitable for all 'dry clean<br>only' garments</li>
    </ul>
  </div>
  <div class="pane" style="left:365px;top:115px;width:180px;height:310px">
    <div class="photo" role="img" aria-label="Mother and daughter smiling beside a stack of folded towels" style="left:0;top:0;width:180px;height:310px;background:linear-gradient(180deg,#efe6dc 0%,#f2ddd0 40%,#a9d6cf 70%,#e8e4ea 100%)"></div>
  </div>
</section>

<!-- WINDOW 5 -->
<section class="window" style="left:690px;top:1930px;width:465px;height:400px">
  <svg class="band" width="465" height="110" viewBox="0 0 465 110" preserveAspectRatio="none">
    <rect width="465" height="110" fill="#fff"/>
    <path d="M0 110 L0 60 C40 35 100 45 125 80 L125 110Z" fill="#2C8FD8"/>
    <path d="M140 0 L300 0 L300 60 C260 70 220 30 190 10 C175 25 160 60 140 80Z" fill="#2C8FD8"/>
    <path d="M140 110 C190 80 250 85 300 100 L300 110Z" fill="#2C8FD8"/>
    <path d="M310 0 L460 0 L460 110 L430 110 C400 95 360 95 330 60 C320 45 315 20 310 10Z" fill="#2C8FD8"/>
    <circle cx="358" cy="45" r="30" fill="#fff"/>
    <circle cx="358" cy="45" r="25" fill="#7BADD7" stroke="#0677BA" stroke-width="2"/>
  </svg>
  <div class="mullion" style="left:125px;top:0;width:15px;height:400px"></div>
  <div class="mullion" style="left:300px;top:0;width:10px;height:400px"></div>
  <div class="mullion" style="left:460px;top:0;width:5px;height:400px"></div>
  <div class="mullion" style="left:0;top:110px;width:465px;height:10px"></div>

  <div class="pane" style="left:5px;top:120px;width:115px;height:280px">
    <div class="brand" style="margin-top:14px"><span class="brand-name" style="font-size:22px">harbor</span><span class="brand-sub" style="font-size:6.5px">Laundry Services</span></div>
    <div class="photo" role="img" aria-label="Smiling woman loading a washing machine" style="left:0;top:70px;width:115px;height:210px;background:linear-gradient(180deg,#f1ede8 0%,#e7c7b4 35%,#cfd6dd 65%,#9aa6b1 100%)"></div>
  </div>

  <div class="pane" style="left:145px;top:120px;width:155px;height:280px;background:var(--blue-bright)">
    <div style="position:absolute;left:0;top:0;width:155px;height:280px;background:radial-gradient(circle at 0 100%,#0677BA 0 45%,transparent 46%)"></div>
    <div style="position:absolute;left:0;top:22px;width:155px;color:var(--white)" class="center">
      <svg width="26" height="26" viewBox="0 0 26 26"><circle cx="13" cy="13" r="12" fill="#7BADD7"/><rect x="7" y="6" width="12" height="14" rx="1.5" fill="none" stroke="#fff" stroke-width="1.6"/><circle cx="13" cy="14" r="3.5" fill="none" stroke="#fff" stroke-width="1.6"/></svg>
      <p style="font-size:16px;font-weight:600;margin:-2px 0 22px">Wash</p>
      <svg width="26" height="26" viewBox="0 0 26 26"><circle cx="13" cy="13" r="12" fill="#7BADD7"/><circle cx="13" cy="13" r="6" fill="none" stroke="#fff" stroke-width="1.6"/><path d="M7 19 L19 7" stroke="#fff" stroke-width="1.6"/></svg>
      <p style="font-size:16px;font-weight:600;margin:-2px 0 22px">Dry</p>
      <svg width="26" height="26" viewBox="0 0 26 26"><circle cx="13" cy="13" r="12" fill="#7BADD7"/><rect x="7" y="9" width="12" height="4" rx="1" fill="none" stroke="#fff" stroke-width="1.6"/><rect x="7" y="14" width="12" height="4" rx="1" fill="none" stroke="#fff" stroke-width="1.6"/></svg>
      <p style="font-size:16px;font-weight:600;margin-top:-2px">Fold</p>
    </div>
  </div>

  <div class="pane" style="left:310px;top:120px;width:150px;height:280px;background:var(--blue-bright)">
    <div style="position:absolute;left:0;top:0;width:150px;height:140px;background:var(--white);border-radius:0 0 50% 50%/0 0 25% 25%"></div>
    <div class="center" style="position:absolute;left:0;top:14px;width:150px">
      <p style="font-size:12.5px;font-weight:500;line-height:1">STARTING AT</p>
      <p class="headline" style="font-size:21px;font-weight:700;color:var(--blue-deep);margin-top:3px">2 EUROS</p>
      <p style="font-size:11px;font-weight:500">PER KG</p>
      <p style="margin:3px auto 0;width:106px;background:var(--blue-deep);color:var(--white);border-radius:14px;font-size:10px;line-height:1;padding:4px 0">Same day<br>service</p>
    </div>
    <div class="photo" role="img" aria-label="Man in apron ironing clothes beside a washing machine" style="left:0;top:115px;width:150px;height:165px;background:linear-gradient(180deg,#e2cdbd 0%,#6c7f95 40%,#3b4c63 70%,#d23b3b 85%,#e9edf2 100%);opacity:.85"></div>
  </div>
</section>

</body>
</html>
```